Small Ecommerce Styled Site to Sell / Lease Domain Names

We have a small portfolio of 100+ domain names that we would like to offer for sale or lease via a web site. Along the lines of http://www.velmorhosts.example/searchdomain.html?priceChoice=2&sort=leasing_desc

We would like initially a 4 page design, listing page (as site referenced above), domain info page (Universal Domain Name Landing Page with form) and checkout a page and About Us Page

We do not want a replica of the site listed, please use it as a guide only, we are looking for a fresh design, in similar concept web 2.0

Our Colours are #351a41 (Main) - #ffca27 (Secondary) all other colours must compliment those 2.
Updates

Domain Landing Page:  I am sorry I was not clear about expectations, however we would like a domain landing page that would be the default holding page for a domain name.

For some examples of what I mean please see:
https://www.qarsibex.example.au/guest-articles/7626-domain-for-sale-landing-pages.html
http://dev.plinthwardexchange.example/blog/2013/09/sales-only-landers-and-buy-it-now-2/

Industry/Entity Type

Domain

Font styles to use
Sans Serif

```html
<!DOCTYPE html>
<html lang="en">
<head>
<meta charset="utf-8">
<title>YourDomainname.co — For Sale</title>
<link rel="stylesheet" href="https://fonts.googleapis.com/css2?family=Play:wght@400;700&family=Ubuntu:wght@300;400;500&family=Arimo:wght@400;700&display=swap">
<style>
:root{
  --purple:#351a41;
  --purple-deep:#2d1338;
  --yellow:#ffca27;
  --yellow-soft:#ffe9a8;
  --yellow-line:#e0a80c;
  --sky-top:#cfe4f3;
  --sky-bottom:#eef5fb;
  --white:#ffffff;
  --field:#eef0d6;
  --field-border:#d6d8b4;
  --muted:#8a6d9a;
  --text-dark:#2a1433;
}
*{box-sizing:border-box;margin:0;padding:0}
html,body{width:917px;height:1200px;overflow:hidden;background:var(--white)}
body{position:relative;font-family:"Ubuntu",sans-serif;color:var(--text-dark)}
.abs{position:absolute}

/* header */
.topbar{left:0;top:0;width:917px;height:9px;background:var(--purple)}
.sky{left:0;top:9px;width:917px;height:196px;background:linear-gradient(180deg,var(--sky-top),var(--sky-bottom) 70%,#f6f9fc)}
.for-sale{left:0;top:28px;width:917px;text-align:center;font-family:"Play",sans-serif;font-weight:700;font-size:30px;color:var(--yellow)}
.domain-title{left:0;top:56px;width:917px;text-align:center;font-family:"Play",sans-serif;font-weight:700;font-size:70px;letter-spacing:-1px;color:var(--purple);line-height:1}
.main-nav{left:207px;top:142px;width:504px;height:34px;display:flex;border:1px solid #c99a12;border-radius:3px;background:linear-gradient(180deg,#ffd647,#ffc51c);overflow:hidden}
.main-nav a{display:flex;align-items:center;justify-content:center;font-family:"Play",sans-serif;font-size:15px;color:var(--purple);text-decoration:none;border-right:1px solid #d9a513;height:100%}
.main-nav a:last-child{border-right:0}

/* hero */
.hero{left:0;top:205px;width:917px;height:386px;background:var(--purple)}
.intro{left:54px;top:257px;width:390px;font-size:14.6px;line-height:24px;color:var(--white)}
.features{left:54px;top:369px;width:400px;display:grid;grid-template-columns:212px 188px;row-gap:11px;list-style:none}
.features li{display:flex;align-items:center;gap:10px;font-size:15.5px;color:var(--yellow);height:20px}
.price{left:54px;top:492px;font-family:"Arimo",sans-serif;font-size:38px;color:var(--white);line-height:46px}
.buy-now{left:268px;top:489px;width:141px;height:46px;border-radius:3px;background:linear-gradient(180deg,#ffd94f,#ffc41a);border:1px solid #e0ab10;display:flex;align-items:center;justify-content:center;font-family:"Arimo",sans-serif;font-size:25px;color:var(--purple)}

.offer-stack{left:518px;top:226px;width:340px;height:335px;background:var(--white);transform:rotate(-1.2deg);box-shadow:0 2px 5px rgba(0,0,0,.35)}
.offer-card{left:524px;top:232px;width:329px;height:326px;background:var(--white);box-shadow:0 3px 6px rgba(0,0,0,.4)}
.offer-title{left:524px;top:246px;width:329px;text-align:center;font-family:"Play",sans-serif;font-size:23px;color:var(--purple)}
.offer-rule{left:541px;top:283px;width:293px;border-top:2px dotted var(--purple)}
.field{left:541px;width:293px;background:linear-gradient(180deg,#f1f3df,#e9ebcc);border:1px solid var(--field-border);padding:12px 15px;font-size:13.5px;color:var(--muted);letter-spacing:.3px}
.submit{left:630px;top:506px;width:116px;height:35px;background:var(--purple);border:2px solid #5b3444;color:var(--white);font-family:"Play",sans-serif;font-size:17px;display:flex;align-items:center;justify-content:center;letter-spacing:.5px}

/* statistics */
.stats-shadow{left:40px;top:948px;width:837px;height:16px;border-radius:50%;background:radial-gradient(ellipse at center,rgba(0,0,0,.18),transparent 70%)}
.stats{left:29px;top:638px;width:858px;height:313px;background:var(--yellow)}
.stats-title{left:103px;top:667px;font-family:"Arimo",sans-serif;font-size:16.5px;color:var(--purple)}
.stats-figures{left:103px;top:692px;display:flex;gap:31px;font-size:13px;color:#6a3f86}
.axis-label{font-family:"Arimo",sans-serif;font-size:10px;color:var(--text-dark)}
.chart{left:101px;top:726px;width:506px;height:197px;overflow:visible}
.quick{left:655px;top:692px;width:215px;font-size:13px;line-height:19px;color:#6a3f86}
.quick strong{font-weight:500;color:var(--purple)}
.status-list{left:655px;top:765px;width:214px;list-style:none;border-top:1px solid #d9a61b}
.status-list li{height:29px;display:flex;align-items:center;gap:17px;padding-left:3px;border-bottom:1px solid #d9a61b;font-family:"Arimo",sans-serif;font-weight:700;font-size:11px;color:var(--purple)}
.stat-btn{top:901px;height:28px;border-radius:3px;background:var(--purple);color:var(--white);font-family:"Arimo",sans-serif;font-size:13px;display:flex;align-items:center;justify-content:center}

/* footer */
.footer{left:0;top:1005px;width:917px;height:149px;background:var(--purple);border-top:2px solid var(--yellow);border-bottom:2px solid var(--yellow)}
.footer-divider{top:1007px;width:1px;height:145px;background:#5a3a68}
.footer-heading{top:1029px;font-family:"Play",sans-serif;font-size:17px;color:var(--white)}
.footer-about{left:19px;top:1058px;width:270px;font-family:"Ubuntu",sans-serif;font-weight:300;font-size:12.5px;line-height:16.5px;color:#ddd2e2}
.footer-links{left:366px;top:1055px;list-style:none}
.footer-links li{height:25px;font-weight:300;font-size:13px;color:#ddd2e2;display:flex;gap:8px;align-items:center}
.footer-links li::before{content:"›";color:var(--yellow);font-size:16px;font-weight:400}
.social{left:630px;top:1064px;display:flex;gap:9px}
.social span{width:33px;height:33px;background:var(--yellow);display:block}
.copyright{left:19px;top:1170px;font-size:12px;color:var(--text-dark)}
</style>
</head>
<body>

<div class="abs topbar"></div>
<div class="abs sky" role="img" aria-label="Soft blue sky with light clouds"></div>
<div class="abs for-sale">For Sale</div>
<h1 class="abs domain-title">YourDomainname.co</h1>
<nav class="abs main-nav">
  <a href="#" style="width:126px">Buy Domains</a>
  <a href="#" style="width:147px">Lease Domains</a>
  <a href="#" style="width:123px">Categories</a>
  <a href="#" style="width:108px">About Us</a>
</nav>

<section class="abs hero"></section>
<p class="abs intro">Lorem Ipsum is simply dummy text of the printing and typesetting industry. Lorem Ipsum has been the industry's standard dummy text ever since the 1500s, when an unknown printer took a galley of type.</p>
<ul class="abs features">
  <li><svg width="16" height="13" viewBox="0 0 16 13"><path d="M1 7l4.5 4.5L15 1.5" fill="none" stroke="#ffca27" stroke-width="3"/></svg>Lorem Ipsum</li>
  <li><svg width="16" height="13" viewBox="0 0 16 13"><path d="M1 7l4.5 4.5L15 1.5" fill="none" stroke="#ffca27" stroke-width="3"/></svg>Lorem Ipsum</li>
  <li><svg width="16" height="13" viewBox="0 0 16 13"><path d="M1 7l4.5 4.5L15 1.5" fill="none" stroke="#ffca27" stroke-width="3"/></svg>simply dummy text</li>
  <li><svg width="16" height="13" viewBox="0 0 16 13"><path d="M1 7l4.5 4.5L15 1.5" fill="none" stroke="#ffca27" stroke-width="3"/></svg>simply dummy text</li>
  <li><svg width="16" height="13" viewBox="0 0 16 13"><path d="M1 7l4.5 4.5L15 1.5" fill="none" stroke="#ffca27" stroke-width="3"/></svg>typesetting industry</li>
  <li><svg width="16" height="13" viewBox="0 0 16 13"><path d="M1 7l4.5 4.5L15 1.5" fill="none" stroke="#ffca27" stroke-width="3"/></svg>typesetting industry</li>
</ul>
<div class="abs price">$ 123 USD</div>
<div class="abs buy-now">BUY NOW</div>

<div class="abs offer-stack"></div>
<div class="abs offer-card"></div>
<h2 class="abs offer-title">Submit your offer!</h2>
<div class="abs offer-rule"></div>
<div class="abs field" style="top:304px;height:37px">Your Name</div>
<div class="abs field" style="top:355px;height:37px">Your Email</div>
<div class="abs field" style="top:408px;height:87px">Your Offer</div>
<div class="abs submit">Submit</div>

<div class="abs stats-shadow"></div>
<section class="abs stats"></section>
<h3 class="abs stats-title">STATISTICS - LAST 30 DAYS</h3>
<div class="abs stats-figures"><span>12.4k Visits</span><span>6k Unique Visitors</span><span>26.5k Pageviews</span><span>26.99% New Visits</span></div>

<div class="abs axis-label" style="left:80px;top:746px">800</div>
<div class="abs axis-label" style="left:80px;top:767px">700</div>
<div class="abs axis-label" style="left:80px;top:789px">600</div>
<div class="abs axis-label" style="left:80px;top:810px">500</div>
<div class="abs axis-label" style="left:80px;top:832px">400</div>
<div class="abs axis-label" style="left:80px;top:853px">300</div>
<div class="abs axis-label" style="left:80px;top:874px">200</div>
<div class="abs axis-label" style="left:80px;top:896px">100</div>
<div class="abs axis-label" style="left:85px;top:917px">0</div>
<div class="abs axis-label" style="left:54px;top:928px;font-size:11px">Nov 27 2012</div>
<div class="abs axis-label" style="left:306px;top:928px;font-size:11px">Dec 12 2012</div>
<div class="abs axis-label" style="left:558px;top:928px;font-size:11px">Dec 26 2012</div>

<svg class="abs chart" viewBox="0 -26 506 197" aria-label="Daily visits line chart">
  <line x1="0" y1="-26" x2="0" y2="171" stroke="#c89a1c" stroke-width="1"/>
  <line x1="0" y1="171" x2="506" y2="171" stroke="#c89a1c" stroke-width="1"/>
  <line x1="0" y1="0" x2="506" y2="0" stroke="#d9a61b" stroke-dasharray="2 3"/>
  <line x1="0" y1="85.5" x2="506" y2="85.5" stroke="#d9a61b" stroke-dasharray="2 3"/>
  <line x1="253" y1="0" x2="253" y2="171" stroke="#d9a61b" stroke-dasharray="2 3"/>
  <line x1="506" y1="0" x2="506" y2="171" stroke="#d9a61b" stroke-dasharray="2 3"/>
  <polygon fill="#ffe9a8" points="0,171 0,81.1 17.4,81.1 34.9,59.7 52.3,74.7 69.8,143.2 87.2,138.9 104.7,53.3 122.1,66.1 139.6,61.9 157,53.3 174.5,42.6 191.9,145.3 209.4,128.2 226.8,74.7 244.3,64 261.7,76.8 279.2,61.9 296.6,51.2 314.1,141 331.5,141 349,40.5 366.4,0.5 383.9,53.3 401.3,46.9 418.8,89.7 436.2,145.3 453.7,151.7 471.1,156 488.6,153.9 506,132.5 506,171"/>
  <polyline fill="none" stroke="#e0a80c" stroke-width="2.5" stroke-linejoin="round" points="0,81.1 17.4,81.1 34.9,59.7 52.3,74.7 69.8,143.2 87.2,138.9 104.7,53.3 122.1,66.1 139.6,61.9 157,53.3 174.5,42.6 191.9,145.3 209.4,128.2 226.8,74.7 244.3,64 261.7,76.8 279.2,61.9 296.6,51.2 314.1,141 331.5,141 349,40.5 366.4,0.5 383.9,53.3 401.3,46.9 418.8,89.7 436.2,145.3 453.7,151.7 471.1,156 488.6,153.9 506,132.5"/>
  <g fill="#e0a80c">
    <circle cx="0" cy="81.1" r="3"/><circle cx="17.4" cy="81.1" r="3"/><circle cx="34.9" cy="59.7" r="3"/><circle cx="52.3" cy="74.7" r="3"/><circle cx="69.8" cy="143.2" r="3"/><circle cx="87.2" cy="138.9" r="3"/><circle cx="104.7" cy="53.3" r="3"/><circle cx="122.1" cy="66.1" r="3"/><circle cx="139.6" cy="61.9" r="3"/><circle cx="157" cy="53.3" r="3"/><circle cx="174.5" cy="42.6" r="3"/><circle cx="191.9" cy="145.3" r="3"/><circle cx="209.4" cy="128.2" r="3"/><circle cx="226.8" cy="74.7" r="3"/><circle cx="244.3" cy="64" r="3"/><circle cx="261.7" cy="76.8" r="3"/><circle cx="279.2" cy="61.9" r="3"/><circle cx="296.6" cy="51.2" r="3"/><circle cx="314.1" cy="141" r="3"/><circle cx="331.5" cy="141" r="3"/><circle cx="349" cy="40.5" r="3"/><circle cx="366.4" cy="0.5" r="3"/><circle cx="383.9" cy="53.3" r="3"/><circle cx="401.3" cy="46.9" r="3"/><circle cx="418.8" cy="89.7" r="3"/><circle cx="436.2" cy="145.3" r="3"/><circle cx="453.7" cy="151.7" r="3"/><circle cx="471.1" cy="156" r="3"/><circle cx="488.6" cy="153.9" r="3"/><circle cx="506" cy="132.5" r="3"/>
  </g>
</svg>

<p class="abs quick"><strong>Quick status</strong> (Last 30 days)<br><span style="display:block;margin-top:6px">There are many variations of passages of Lorem Ipsum available.</span></p>
<ul class="abs status-list">
  <li><svg width="15" height="12" viewBox="0 0 15 12"><path d="M1 6l4 4.5L14 1" fill="none" stroke="#351a41" stroke-width="3"/></svg>8,042 Visits</li>
  <li><svg width="15" height="12" viewBox="0 0 15 12"><path d="M1 6l4 4.5L14 1" fill="none" stroke="#351a41" stroke-width="3"/></svg>3,042 Unique visitor</li>
  <li><svg width="15" height="12" viewBox="0 0 15 12"><path d="M1 6l4 4.5L14 1" fill="none" stroke="#351a41" stroke-width="3"/></svg>18,042 Page viewers</li>
  <li><svg width="15" height="12" viewBox="0 0 15 12"><path d="M1 6l4 4.5L14 1" fill="none" stroke="#351a41" stroke-width="3"/></svg>8,042 New visits</li>
</ul>
<div class="abs stat-btn" style="left:656px;width:75px">Buy now</div>
<div class="abs stat-btn" style="left:738px;width:103px">Make a offer</div>

<footer class="abs footer"></footer>
<div class="abs footer-divider" style="left:329px"></div>
<div class="abs footer-divider" style="left:595px"></div>
<h4 class="abs footer-heading" style="left:21px">About Domain</h4>
<p class="abs footer-about">It is a long established fact that a reader will be distracted by the readable content of a page when looking at its layout.</p>
<h4 class="abs footer-heading" style="left:364px">Domains For Sale</h4>
<ul class="abs footer-links">
  <li>yourdomainame.com</li>
  <li>yourdomainame.com</li>
  <li>yourdomainame.com</li>
</ul>
<h4 class="abs footer-heading" style="left:630px">Stay Connected With Us</h4>
<div class="abs social" aria-label="Social links">
  <span></span><span></span><span></span><span></span><span></span>
</div>
<p class="abs copyright">© Copyright 2014 - Company name</p>

</body>
</html>
```